Corvane Supplies Business Card

Professional business card that stand out to our potential customers. Front and back with clean modern design

Industry/Entity Type

Oil and gas

Contact Information for Business Card

Name, address, website , office phone and cell number

Requirements
Must have
• Editable files for each employee

```html
<!DOCTYPE html>
<html lang="en">
<head>
<meta charset="utf-8">
<title>Corvane Supplies Business Card</title>
<link href="https://fonts.googleapis.com/css2?family=Montserrat:wght@400;500;700;800&display=swap" rel="stylesheet">
<style>
  :root {
    --stage: #3a3a3c;
    --card-dark: #1b1418;
    --brand-red: #e8121c;
    --brand-blue: #12b4d4;
    --ink-light: #f2f2f2;
    --deep-red: #5a1a1e;
    --deep-teal: #1e3a44;
  }
  * { margin: 0; padding: 0; box-sizing: border-box; }
  html, body { width: 1200px; height: 900px; overflow: hidden; }
  body {
    background: var(--stage);
    font-family: "Montserrat", Arial, sans-serif;
    display: flex;
    align-items: center;
    justify-content: center;
    gap: 60px;
  }
  .card {
    width: 380px;
    height: 650px;
    border-radius: 22px;
    background: var(--card-dark);
    position: relative;
    overflow: hidden;
  }
  /* Front */
  .front-decoration {
    position: absolute;
    inset: 0;
    background: linear-gradient(160deg, var(--brand-blue) 0%, var(--brand-blue) 28%, var(--card-dark) 40%, var(--brand-red) 55%, var(--brand-red) 80%, var(--card-dark) 100%);
  }
  .front-wordmark {
    position: absolute;
    right: 28px;
    bottom: 34px;
    display: flex;
    align-items: center;
    gap: 8px;
    background: var(--card-dark);
    padding: 6px 10px;
  }
  .wordmark-square {
    width: 12px;
    height: 12px;
    background: var(--brand-blue);
  }
  .wordmark-text {
    font-weight: 800;
    font-size: 17px;
    letter-spacing: 1px;
    text-transform: uppercase;
    color: var(--brand-red);
    white-space: nowrap;
  }
  /* Back */
  .back-decoration {
    position: absolute;
    inset: 0;
    background:
      linear-gradient(180deg, var(--deep-teal) 0%, var(--deep-teal) 30%, transparent 45%),
      linear-gradient(200deg, var(--deep-red) 0%, var(--card-dark) 60%, var(--deep-red) 100%);
    opacity: .85;
  }
  .back-content {
    position: relative;
    height: 100%;
  }
  .back-wordmark {
    position: absolute;
    top: 185px;
    left: 0;
    right: 0;
    display: flex;
    justify-content: center;
    align-items: center;
    gap: 10px;
  }
  .back-wordmark .wordmark-text { font-size: 20px; }
  .holder {
    position: absolute;
    top: 310px;
    left: 50px;
  }
  .holder-name {
    font-weight: 800;
    font-size: 17px;
    color: var(--brand-red);
    text-transform: uppercase;
  }
  .holder-title {
    font-weight: 700;
    font-size: 12px;
    color: var(--brand-blue);
    text-transform: uppercase;
    margin-left: 6px;
  }
  .contact-list {
    list-style: none;
    position: absolute;
    top: 378px;
    left: 58px;
    color: var(--ink-light);
    font-size: 15px;
  }
  .contact-list li { display: flex; align-items: center; gap: 10px; line-height: 22px; }
  .contact-list svg { width: 12px; height: 12px; fill: var(--brand-blue); flex: none; }
  .address {
    position: absolute;
    top: 460px;
    left: 70px;
    color: var(--ink-light);
    font-size: 13px;
    font-style: normal;
    line-height: 19px;
  }
  .website {
    position: absolute;
    top: 520px;
    left: 70px;
    color: var(--brand-blue);
    font-size: 15px;
    font-weight: 500;
  }
</style>
</head>
<body>
  <section class="card card-front">
    <div class="front-decoration" role="img" aria-label="Large angular brand decoration in blue and red"></div>
    <div class="front-wordmark">
      <span class="wordmark-square"></span>
      <span class="wordmark-text">Corvane Supplies</span>
    </div>
  </section>

  <section class="card card-back">
    <div class="back-decoration" role="img" aria-label="Faint angular decoration in teal and dark red"></div>
    <div class="back-content">
      <div class="back-wordmark">
        <span class="wordmark-square"></span>
        <span class="wordmark-text">Corvane Supplies</span>
      </div>
      <div class="holder">
        <div class="holder-name">Marcus Delaney</div>
        <div class="holder-title">Managing Director</div>
      </div>
      <ul class="contact-list">
        <li>
          <svg viewBox="0 0 12 12"><path d="M2 1h3l1 3-1.5 1a7 7 0 0 0 2.5 2.5L8 6l3 1v3a1 1 0 0 1-1 1A9 9 0 0 1 1 2a1 1 0 0 1 1-1z"/></svg>
          432 617 20 95
        </li>
        <li>
          <svg viewBox="0 0 12 12"><path d="M3 0h6a1 1 0 0 1 1 1v10a1 1 0 0 1-1 1H3a1 1 0 0 1-1-1V1a1 1 0 0 1 1-1zm0 2v7h6V2z"/></svg>
          432 908 14 63
        </li>
        <li>
          <svg viewBox="0 0 12 12"><path d="M0 2h12v1L6 7 0 3zm0 2.5l6 4 6-4V10H0z"/></svg>
          info@corvanesupplies.com
        </li>
      </ul>
      <address class="address">
        48 Harlan Road<br>
        Midvale, Texas 79701
      </address>
      <div class="website">www.corvanesupplies.com</div>
    </div>
  </section>
</body>
</html>
```